Landingpage Design X-Mas Invitation

Every year we invite customers to a special X-Mas Apéro. Since we are an IT-Company we handle the registration process by a landingpage. For this we need a design for the event 2016. The content will be the same as 2015 (you will finde the design attached from last year. There will be an additional job for creating the E-Mail.

Target Market(s)

Customers of IT Company, medium Companys in Central Switzerland

Industry/Entity Type

It Company

Number of Pages Required

1 page

Requirements
Must have
• Christmas Style

```html
<!DOCTYPE html>
<html lang="de">
<head>
<meta charset="utf-8">
<title>Helvion Weihnachts apéro</title>
<link rel="stylesheet" href="https://fonts.googleapis.com/css2?family=Lora:wght@400;700&display=swap">
<style>
  :root {
    --red: #e42a30;
    --red-light: #f2383e;
    --red-dark: #c81e26;
    --white: #ffffff;
    --line: rgba(255,255,255,0.35);
    --button: #b81c22;
    --partner: rgba(120,20,24,0.55);
    --tree-light: rgba(140,197,64,0.95);
    --tree-mid: rgba(90,168,56,0.75);
    --tree-fade: rgba(63,154,56,0);
  }
  * { box-sizing: border-box; margin: 0; padding: 0; }
  html, body { width: 1200px; height: 674px; overflow: hidden; }
  body {
    position: relative;
    font-family: "Lora", Georgia, serif;
    color: var(--white);
    background: radial-gradient(ellipse at 30% 20%, var(--red-light), var(--red) 55%, var(--red-dark));
  }
  .brand {
    position: absolute; left: 67px; top: 48px;
    font-weight: 700; font-size: 34px; line-height: 1;
  }
  .brand small {
    display: block; text-align: right;
    font-weight: 400; font-size: 11px; letter-spacing: 0.5px; margin-top: 2px;
  }
  .event { position: absolute; left: 67px; top: 150px; }
  .event-title { font-weight: 400; font-size: 41px; line-height: 49px; }
  .divider { width: 61px; height: 1px; background: var(--line); margin: 24px 0; }
  .event-info { font-size: 21px; line-height: 33px; }
  .tree {
    position: absolute; left: 259px; top: 70px; width: 386px; height: 468px;
    background: radial-gradient(ellipse 50% 55% at 50% 55%, var(--tree-light), var(--tree-mid) 55%, var(--tree-fade) 100%);
  }
  .registration { position: absolute; left: 680px; top: 45px; width: 455px; }
  .intro { font-size: 12.5px; line-height: 24px; }
  .form-heading { font-weight: 700; font-size: 13px; line-height: 16px; }
  .form-heading.first { margin: 28px 0 30px; }
  .form-heading.second { margin: 12px 0 36px; }
  .field {
    font-size: 9.5px; line-height: 13px; padding-bottom: 4px;
    border-bottom: 1px solid var(--line); margin-bottom: 23px;
  }
  .actions { display: flex; gap: 24px; margin-top: 15px; }
  .button {
    background: var(--button); color: var(--white);
    font-family: inherit; font-weight: 700; font-size: 10px;
    padding: 9px 11px; border: 0;
  }
  .partners {
    position: absolute; left: 67px; top: 610px; width: 1108px;
    display: flex; justify-content: space-between; align-items: center;
  }
  .partner { width: 48px; height: 14px; background: var(--partner); border-radius: 2px; }
  .partner.round { width: 20px; height: 20px; border-radius: 50%; }
</style>
</head>
<body>
  <div class="brand">Helvion<small>IT SOLUTIONS</small></div>

  <section class="event">
    <h1 class="event-title">Helvion<br>Weihnachts<br>apéro</h1>
    <div class="divider"></div>
    <p class="event-info">17. Dezember 2015<br>17 – &nbsp;20 &nbsp;Uhr</p>
    <div class="divider"></div>
    <p class="event-info">Sternensaal<br>Lindenhofstrasse 12<br>Luzern</p>
  </section>

  <div class="tree" role="img" aria-label="Illustration eines Weihnachtsbaums aus grünem Papierband, umgeben von goldenen Schneeflocken"></div>

  <section class="registration">
    <p class="intro">Ob Sie den ganzen Abend bleiben oder nur kurz nach dem Weihnachts-Shopping vorbeischauen, ist ganz Ihnen überlassen.<br>Wir freuen uns sehr, wenn Sie uns die Gelegenheit geben, Ihnen mit dieser Einladung für die erfolgreiche Zusammenarbeit herzlichst zu danken.</p>

    <h2 class="form-heading first">Ihre Anmeldung</h2>
    <div class="field">Ihre E-Mail-Adresse</div>
    <div class="field">Vorname</div>
    <div class="field">Nachname</div>

    <h2 class="form-heading second">Ihre Begleitperson</h2>
    <div class="field">Ihre E-Mail-Adresse</div>
    <div class="field">Vorname</div>
    <div class="field">Nachname</div>

    <div class="actions">
      <button class="button">Weitere Begleitperson</button>
      <button class="button">Absenden</button>
    </div>
  </section>

  <div class="partners" aria-label="Partner">
    <span class="partner round"></span>
    <span class="partner"></span>
    <span class="partner"></span>
    <span class="partner"></span>
    <span class="partner"></span>
    <span class="partner"></span>
    <span class="partner"></span>
    <span class="partner"></span>
    <span class="partner"></span>
    <span class="partner"></span>
    <span class="partner"></span>
  </div>
</body>
</html>
```